Robotic Physical Therapy office needs a Grand Opening Flyer

We need a Grand Opening flyer design for a robotic physical therapy office named Stellar Motion Therapy. We would like it to have a clean, classy, upscale feeling that gives potential clients a V.I.P. feeling. We would like to use the colors black, gray, and yellow (logo will be uploaded).

Event: Thursday, June 1st, 2023 from 12pm-6pm
location: 58274 Harlow Ave, Bloomfield Hills, MI 48319

Industry/Entity Type

Physical therapy

Font styles to use
Script

Colors

Designer to choose colors to be used in the design.

Requirements
Nice to have
• More of a vip feel for the invite

```html
<!DOCTYPE html>
<html lang="en">
<head>
<meta charset="utf-8">
<title>Stellar Motion Therapy – Grand Opening</title>
<link rel="stylesheet" href="https://fonts.googleapis.com/css2?family=Roboto:wght@400;500;700&display=swap">
<style>
  :root {
    --page: #e4e4e6;
    --card: #2c2b31;
    --card-deep: #232228;
    --yellow: #f5dc2c;
    --olive: #4a4520;
    --white: #ffffff;
    --ink: #1f1e22;
    --photo-a: #d9dadd;
    --photo-b: #8b8f96;
  }
  * { box-sizing: border-box; margin: 0; padding: 0; }
  html, body {
    width: 1200px; height: 900px; overflow: hidden;
    background: var(--page);
    font-family: "Roboto", Arial, sans-serif;
  }
  .flyer {
    position: absolute; left: 50px; top: 175px;
    width: 1100px; height: 550px;
    background: linear-gradient(120deg, var(--card) 0%, var(--card-deep) 100%);
    overflow: hidden;
    box-shadow: 0 10px 30px rgba(0,0,0,.25);
  }
  .accent-block {
    position: absolute; left: 0; top: 0; width: 215px; height: 290px;
    background: var(--olive);
  }
  .backdrop-lines { position: absolute; inset: 0; }
  .photo-dot {
    position: absolute; left: 340px; top: 370px; width: 100px; height: 100px;
    border-radius: 50%; background: var(--yellow);
  }
  .photo {
    position: absolute; left: 30px; top: 100px; width: 400px; height: 400px;
    border-radius: 50%;
    background: radial-gradient(circle at 40% 40%, var(--photo-a) 0%, var(--photo-b) 100%);
  }
  .photo-ring { position: absolute; left: 30px; top: 100px; width: 400px; height: 400px; }
  .corner-dot {
    position: absolute; left: 985px; top: 455px; width: 120px; height: 120px;
    border-radius: 50%; background: var(--yellow);
  }
  .brand {
    position: absolute; right: 150px; top: 48px;
    display: flex; align-items: center; gap: 14px;
  }
  .brand-mark { width: 58px; height: 58px; border-radius: 50%; background: var(--white); }
  .brand-name {
    color: var(--yellow); font-weight: 700; font-size: 34px; line-height: 1;
    text-transform: uppercase;
  }
  .headline {
    position: absolute; right: 150px; top: 170px;
    color: var(--white); font-weight: 700; font-size: 60px; letter-spacing: .5px;
  }
  .name-band {
    position: absolute; left: 455px; top: 250px; width: 510px; height: 84px;
    background: var(--yellow);
    display: flex; align-items: center; justify-content: center;
  }
  .name-band span { color: var(--ink); font-weight: 500; font-size: 50px; }
  .event-date {
    position: absolute; right: 150px; top: 360px;
    color: var(--white); font-size: 22px; font-weight: 500; letter-spacing: 2.5px;
  }
  .event-place {
    position: absolute; right: 150px; top: 398px;
    color: var(--yellow); font-size: 14px; font-weight: 500; letter-spacing: 1.5px;
  }
  .social { position: absolute; right: 150px; top: 440px; display: flex; gap: 10px; }
  .social span { width: 24px; height: 24px; border-radius: 50%; border: 1.5px solid var(--white); }
  .website {
    position: absolute; right: 150px; top: 490px;
    color: var(--white); font-size: 15px; letter-spacing: 2px;
  }
</style>
</head>
<body>
  <section class="flyer">
    <div class="accent-block"></div>
    <svg class="backdrop-lines" width="1100" height="550" viewBox="0 0 1100 550">
      <path d="M120 540 C 300 420, 480 420, 620 520" fill="none" stroke="#f5dc2c" stroke-width="1" opacity=".6"/>
    </svg>
    <div class="photo-dot"></div>
    <div class="photo" role="img" aria-label="Photo of a patient's legs in a robotic gait-training exoskeleton on a treadmill"></div>
    <svg class="photo-ring" viewBox="0 0 400 400">
      <g fill="none" stroke="#fff" stroke-width="3" stroke-linecap="round">
        <path d="M200 30 A170 170 0 0 1 330 90"/>
        <path d="M360 170 A170 170 0 0 1 350 260"/>
        <path d="M300 340 A170 170 0 0 1 180 368"/>
        <path d="M90 330 A170 170 0 0 1 34 220"/>
        <path d="M40 150 A170 170 0 0 1 120 52"/>
      </g>
    </svg>
    <div class="corner-dot"></div>

    <div class="brand">
      <span class="brand-mark"></span>
      <span class="brand-name">Stellar Motion<br>Therapy</span>
    </div>
    <h1 class="headline">GRAND OPENING</h1>
    <div class="name-band"><span>Stellar Motion Therapy</span></div>
    <p class="event-date">THURSDAY, JUNE 1ST, 2023 FROM 12PM-6PM</p>
    <p class="event-place">58274 HARLOW AVE, BLOOMFIELD HILLS, MI 48319</p>
    <div class="social"><span></span><span></span><span></span></div>
    <p class="website">www.stellarmotiontherapy.com</p>
  </section>
</body>
</html>
```